Calma Rosa_4 Page Brochure (8-1/2"x 11)

Create a 4 -page brochure (8-1/2"x11 each page) in the exact likeness of the Silent auction piece. Instead of "bid to win" it will be " Redeem for a Complimentary"...Luxury Landscape Plan.
Expand brochure to show more/larger images of work./ description of services /portfolio (content can be duplicated from website)

```html
<!DOCTYPE html>
<html lang="en">
<head>
<meta charset="utf-8">
<title>Calma Rosa – Luxury Landscape Plan Brochure</title>
<link href="https://fonts.googleapis.com/css2?family=Montserrat:wght@400;500;600;700;800&family=Cormorant+Garamond:wght@500&display=swap" rel="stylesheet">
<style>
:root{
  --bg:#8e8e8e;
  --dark:#222221;
  --charcoal:#2e2d2b;
  --gold:#c9a85a;
  --gold-light:#e3cf8e;
  --gold-deep:#a88a3e;
  --orange:#c98a2a;
  --green:#2f7a3a;
  --paper:#f1f1f0;
  --text-light:#d9d6cf;
  --text-grey:#cfcfcf;
}
*{box-sizing:border-box;margin:0;padding:0}
html,body{width:1200px;height:474px;overflow:hidden;background:var(--bg);font-family:"Montserrat",sans-serif}
.stage{position:relative;width:1200px;height:474px}
.page{position:absolute;top:86px;height:322px;overflow:hidden;box-shadow:0 3px 6px rgba(0,0,0,.35)}
.abs{position:absolute}

/* ---------- Front cover ---------- */
.cover{left:76px;width:245px;background:var(--dark)}
.cover-top{left:0;top:0;width:245px;height:85px;background:#fff}
.cover-brand{left:22px;top:30px;color:var(--green);font-weight:600;font-size:15px;letter-spacing:.5px;display:flex;align-items:center;gap:6px}
.cover-brand .dot{width:12px;height:12px;border-radius:50%;background:var(--green)}
.cover-tag{left:40px;top:50px;font-size:3.4px;letter-spacing:.8px;color:var(--green);font-weight:600}
.cover-photo{left:0;top:85px;width:245px;height:130px;
  background:
    radial-gradient(ellipse 38% 22% at 52% 38%,#ffd9a0 0%,#f0a858 40%,rgba(180,110,50,0) 100%),
    radial-gradient(ellipse 60% 26% at 50% 78%,#d07ae8 0%,#8a3fc0 40%,rgba(60,25,90,0) 100%),
    linear-gradient(180deg,#1b2420 0%,#2a2c24 40%,#3a2a40 70%,#2a1b38 100%)}
.cover-offer{left:0;width:245px;top:231px;text-align:center;color:var(--gold)}
.offer-lead{font-size:7px;font-weight:400}
.offer-title{font-family:"Cormorant Garamond",serif;font-size:22px;line-height:1;margin-top:4px;color:var(--gold-light)}
.offer-plan{display:flex;align-items:center;justify-content:center;gap:6px;font-size:10px;letter-spacing:6px;margin-top:1px;color:var(--gold-light)}
.offer-plan i{display:block;width:55px;height:.6px;background:var(--gold)}
.cover-url{right:17px;bottom:14px;font-size:5px;color:#eee;letter-spacing:.3px}

/* ---------- Spread ---------- */
.portfolio{left:353px;width:245px;background:#0c0c0c}
.portfolio-hero{left:0;top:0;width:245px;height:205px;
  background:
    radial-gradient(ellipse 30% 20% at 70% 38%,#9fb6c8 0%,rgba(120,140,160,0) 100%),
    radial-gradient(ellipse 55% 35% at 55% 45%,#c7a47a 0%,#9a7a58 45%,rgba(90,70,50,0) 100%),
    linear-gradient(180deg,#56657a 0%,#8c7a66 25%,#7a6048 50%,#3a2e24 75%,#0c0c0c 100%)}
.portfolio-title{left:0;width:245px;top:15px;text-align:center;font-weight:800;font-size:24px;letter-spacing:1.5px;color:var(--gold-light);text-shadow:0 1px 3px rgba(0,0,0,.5)}
.tile{transform:skewX(-10deg);border:1.6px solid #fff;box-shadow:0 2px 4px rgba(0,0,0,.5)}
.tile-a{left:16px;top:117px;width:64px;height:58px;background:linear-gradient(170deg,#7c8a6a 0%,#5a6848 35%,#b8443a 65%,#6a3b2a 100%)}
.tile-b{left:77px;top:100px;width:88px;height:84px;background:radial-gradient(ellipse 30% 25% at 45% 75%,#ffb050 0%,rgba(200,110,40,0) 100%),linear-gradient(160deg,#5d6b48 0%,#7a5a44 45%,#8a5a3b 70%,#4a3a30 100%)}
.tile-c{left:164px;top:109px;width:74px;height:64px;background:linear-gradient(165deg,#8a7a60 0%,#6b5da8 30%,#8577c8 50%,#d84a6e 78%,#5c8a48 100%)}
.services{left:31px;top:198px;display:grid;grid-template-columns:105px 90px;row-gap:2.4px;font-size:7.2px;color:#fff}
.services li{list-style:none;display:flex;align-items:center;gap:4px;white-space:nowrap}
.services li::before{content:"✓";display:inline-flex;align-items:center;justify-content:center;width:5px;height:5px;border:.6px solid #fff;font-size:4px;line-height:1}
.portfolio-foot{left:0;top:248px;width:245px;height:74px;
  background:
    radial-gradient(ellipse 30% 40% at 30% 65%,#8a5a34 0%,rgba(110,70,40,0) 100%),
    radial-gradient(ellipse 35% 45% at 70% 70%,#7a7a70 0%,rgba(80,80,70,0) 100%),
    linear-gradient(180deg,#0c0c0c 0%,#2e2a22 35%,#4a3a2a 70%,#5a3e26 100%)}

.process{left:598px;width:245px;background:var(--paper)}
.step{left:17px;width:218px;display:flex;gap:6px}
.step-photo{flex:0 0 51px;height:36px;border:1px solid #fff;box-shadow:0 0 1.5px rgba(0,0,0,.45)}
.step h3{font-size:7.5px;font-weight:700;color:var(--orange);letter-spacing:.2px;margin-top:-1px}
.step p{font-size:3.3px;line-height:1.35;color:#333;margin-top:1.5px}
.step-1{top:13px}.step-1 .step-photo{background:linear-gradient(120deg,#c9b49a 0%,#6e88a8 35%,#e0c4a8 60%,#7a6450 100%)}
.step-2{top:64px}.step-2 .step-photo{background:radial-gradient(ellipse 30% 35% at 40% 50%,#e9d9a0 0%,rgba(230,210,150,0) 100%),linear-gradient(120deg,#6aae44 0%,#e2c45a 45%,#e06a52 75%,#7ab84e 100%)}
.step-3{top:115px}.step-3 .step-photo{background:linear-gradient(150deg,#9e9a92 0%,#6f6a62 35%,#c8c2b4 65%,#8a867e 100%)}
.reviews-band{left:0;top:176px;width:245px;height:22px;background:linear-gradient(90deg,var(--gold-deep),var(--gold),var(--gold-deep));color:#fff;font-size:8px;font-weight:600;display:flex;align-items:center;justify-content:center}
.reviews{left:0;top:198px;width:245px;height:124px;background:var(--charcoal)}
.review{left:43px;width:160px;color:var(--text-grey);font-size:3.7px;line-height:1.5}
.review .q{color:var(--gold);font-weight:800;font-size:8px;font-style:italic;line-height:0;margin-right:2px}
.review .meta{display:flex;justify-content:space-between;margin-top:4px;color:var(--gold);font-size:4px}
.review .stars{letter-spacing:.5px}
.review-1{top:10px}.review-2{top:62px}

/* ---------- Back ---------- */
.back{left:876px;width:245px;background:var(--dark)}
.back-corner{right:0;top:0}
.back-title{left:11px;top:9px;color:var(--gold-light);font-weight:600;font-size:6.5px}
.back-sub{left:11px;top:18px;color:#fff;font-size:4.2px}
.back-sub span{color:var(--gold-light)}
.portrait{left:11px;top:32px;width:34px;height:50px;background:linear-gradient(180deg,#7a8088 0%,#55606c 50%,#2e3540 100%)}
.bio{left:51px;top:32px;width:182px;color:var(--text-light);font-size:3.2px;line-height:1.45}
.bio p+p{margin-top:3px}
.plan{left:13px;top:87px;width:219px;height:126px;border:1px solid #444;
  background:
    radial-gradient(ellipse 17% 14% at 38% 30%,#7ab8e8 0%,#9cc8e8 50%,rgba(200,190,160,0) 100%),
    radial-gradient(ellipse 20% 30% at 82% 30%,#b8d890 0%,rgba(180,210,140,0) 100%),
    radial-gradient(ellipse 12% 40% at 4% 50%,#4e9a3e 0%,rgba(80,150,60,0) 100%),
    radial-gradient(ellipse 40% 12% at 55% 92%,#5ea84a 0%,rgba(90,160,70,0) 100%),
    linear-gradient(135deg,#cfc0a2 0%,#d9cbb0 50%,#c9b898 100%)}
.gallery{left:15px;top:223px;display:flex;gap:3px}
.gallery div{width:70px;height:47px}
.g1{background:radial-gradient(ellipse 45% 35% at 40% 70%,#e0384a 0%,rgba(200,50,60,0) 100%),linear-gradient(160deg,#8a7a6a 0%,#5a6e42 55%,#3e5a2e 100%)}
.g2{background:radial-gradient(ellipse 30% 25% at 50% 75%,#ffb060 0%,rgba(220,130,60,0) 100%),linear-gradient(170deg,#8a3e1e 0%,#c46a32 45%,#5a2a16 100%)}
.g3{background:radial-gradient(ellipse 35% 30% at 45% 65%,#d9b070 0%,rgba(200,160,100,0) 100%),linear-gradient(160deg,#6a8a3e 0%,#8a7a4a 55%,#3e3a28 100%)}
.back-rule{left:0;top:277px;width:245px;height:.8px;background:var(--gold-deep)}
.contact{top:291px;color:#fff;font-size:4.8px;display:flex;align-items:center;gap:2px}
.contact-phone{left:11px}.contact-web{left:67px}
.badge{top:284px;height:20px;background:#e8e8e6}
.badge-1{left:135px;width:42px}.badge-2{left:181px;width:40px}.badge-3{left:225px;width:11px}
.back-stripe{left:0;bottom:0;width:245px;height:8px;background:linear-gradient(90deg,var(--gold-deep),var(--gold-light),var(--gold-deep))}
</style>
</head>
<body>
<main class="stage">

  <section class="page cover">
    <div class="abs cover-top"></div>
    <div class="abs cover-photo" role="img" aria-label="Night view of a lit pool house with outdoor kitchen above a glowing purple pool"></div>
    <svg class="abs" style="left:0;top:0" width="245" height="215" viewBox="0 0 245 215">
      <polygon points="140,0 245,0 245,85 180,85" fill="#c9a85a"/>
      <polygon points="180,85 245,85 245,215 170,215" fill="#3a3328" opacity=".45"/>
      <polygon points="0,85 30,85 0,140" fill="#1a1a18" opacity=".45"/>
    </svg>
    <div class="abs cover-brand"><span class="dot"></span>Calma Rosa</div>
    <div class="abs cover-tag">LANDSCAPE DESIGN &amp; CONSTRUCTION</div>
    <svg class="abs" style="left:0;top:215px" width="245" height="107" viewBox="0 0 245 107">
      <polygon points="0,0 70,0 0,75" fill="#3a3935"/>
      <polygon points="0,107 50,50 95,107" fill="#4a4946"/>
    </svg>
    <div class="abs cover-offer">
      <div class="offer-lead">Redeem for a Complimentary</div>
      <div class="offer-title">Luxury Landscape</div>
      <div class="offer-plan"><i></i>PLAN<i></i></div>
    </div>
    <div class="abs cover-url">www.calmarosaco.com</div>
  </section>

  <section class="page portfolio">
    <div class="abs portfolio-hero" role="img" aria-label="Stone luxury estate home at dusk"></div>
    <h1 class="abs portfolio-title">PORTFOLIO</h1>
    <div class="abs tile tile-a" role="img" aria-label="Patio seating with red cushions overlooking mountains"></div>
    <div class="abs tile tile-b" role="img" aria-label="Outdoor fireplace and fire pit patio"></div>
    <div class="abs tile tile-c" role="img" aria-label="Stone walls with purple and pink flower beds"></div>
    <div class="abs portfolio-foot" role="img" aria-label="Wooden footbridge over a rock garden stream"></div>
    <ul class="abs services">
      <li>Landscaping</li><li>Fireplaces &amp; Firepits</li>
      <li>Hardscaping</li><li>Garden Structures</li>
      <li>Outdoor Living &amp; Dining</li><li>Masonry</li>
      <li>Outdoor Kitchens</li><li>Recreation</li>
      <li>Water Features &amp; Pools</li>
    </ul>
  </section>

  <section class="page process">
    <div class="abs step step-1">
      <div class="step-photo" role="img" aria-label="Designers reviewing plans with homeowners"></div>
      <div><h3>CONSULTATION</h3>
      <p>At Calma Rosa our journey begins with an immersive consultation tailored to your unique aspirations. Our seasoned team of landscape architects and designers will personally engage with you to understand your lifestyle, preferences, and dreams. This initial phase is not just a meeting; it's a creative collaboration, where we blend your vision with our expertise to conceptualize an outdoor masterpiece, ensuring a truly bespoke experience.</p></div>
    </div>
    <div class="abs step step-2">
      <div class="step-photo" role="img" aria-label="Colour landscape design plan"></div>
      <div><h3>LANDSCAPE DESIGN</h3>
      <p>With your vision firmly in our grasp, our skilled designers meticulously craft a breathtaking landscape design that captures the essence of luxury living. Every detail, from the placement of exquisite flora to the selection of premium materials, is curated to elevate your outdoor space to unparalleled heights. Our commitment to excellence ensures that your personalized design not only reflects your style but enhances the beauty of your residence.</p></div>
    </div>
    <div class="abs step step-3">
      <div class="step-photo" role="img" aria-label="Crew laying stone pavers on site"></div>
      <div><h3>CONSTRUCTION</h3>
      <p>As the sun sets on the design phase, the construction journey begins, transforming your dreams into a tangible masterpiece. Our seasoned craftsmen, selected for their unwavering dedication to precision, meticulously bring the design to life. Impeccable stonework, lush greenery, and bespoke water features materialize under the skillful hands of our artisans. Rest assured, our commitment to excellence ensures that the final result will surpass even the loftiest expectations.</p></div>
    </div>
    <div class="abs reviews-band">Discover What Our Customers Love About Us</div>
    <div class="abs reviews">
      <blockquote class="abs review review-1">
        <span class="q">//</span>"Marcus was so great to work with! He always responded promptly to our calls, emails, and the work was completed in a timely manner. Our project was fairly small but we always felt he treated it with all the importance of a large project. Very professional! We would highly recommend him!" <span class="q">//</span>
        <div class="meta"><span class="stars">★★★★★</span><span>Helen Corwick</span></div>
      </blockquote>
      <blockquote class="abs review review-2">
        <span class="q">//</span>Marcus and his team did a fabulous job updating our entire backyard. Marcus communicated frequently with us during the course of the project and completed the job on time. His team was extremely professional and maintained a thoughtful, close attention to detail. I also really appreciated being able to rely on his design eye for a beautifully finished project! <span class="q">//</span>
        <div class="meta"><span class="stars">★★★★★</span><span>Priya</span></div>
      </blockquote>
    </div>
  </section>

  <section class="page back">
    <svg class="abs back-corner" width="40" height="70" viewBox="0 0 40 70">
      <polygon points="0,0 40,0 40,50" fill="#f1f1f0"/>
      <polygon points="0,0 40,50 40,70" fill="#4a463e"/>
    </svg>
    <h2 class="abs back-title">Luxury Landscape Plan</h2>
    <div class="abs back-sub">by Award Winning Landscape designer <span>Marcus L. Whitfield, RLA</span></div>
    <div class="abs portrait" role="img" aria-label="Portrait of the lead landscape designer"></div>
    <div class="abs bio">
      <p>With over 30 years of acclaimed landscape design experience, Marcus L. Whitfield is celebrated for his transformative landscape designs that harmonize natural beauty with architectural elegance. His visionary work has graced prestigious luxury homes &amp; estates nationwide. He has been featured in both local and national magazine publications.</p>
      <p>Marcus's expertise has also been showcased on the Home Craft Channel, where he has shared his innovative approach to sustainable landscaping. His commitment to creating enduring, awe-inspiring landscapes makes his donation piece a testament to both his talent and dedication to environmental stewardship.</p>
    </div>
    <div class="abs plan" role="img" aria-label="Conceptual landscape plan with pool, patios, pergola and lawn areas"></div>
    <div class="abs gallery">
      <div class="g1" role="img" aria-label="Red flower beds by a stone home"></div>
      <div class="g2" role="img" aria-label="Covered outdoor room with fire pit at night"></div>
      <div class="g3" role="img" aria-label="Garden courtyard with fountain"></div>
    </div>
    <div class="abs back-rule"></div>
    <div class="abs contact contact-phone">
      <svg width="5" height="5" viewBox="0 0 24 24"><path fill="#fff" d="M6.6 10.8a15 15 0 006.6 6.6l2.2-2.2c.3-.3.7-.4 1-.2 1.1.4 2.3.6 3.6.6.6 0 1 .4 1 1V20c0 .6-.4 1-1 1A17 17 0 013 4c0-.6.4-1 1-1h3.5c.6 0 1 .4 1 1 0 1.3.2 2.5.6 3.6.1.3 0 .7-.2 1z"/></svg>(555) 014-0820
    </div>
    <div class="abs contact contact-web">
      <svg width="5" height="5" viewBox="0 0 24 24" fill="none" stroke="#fff" stroke-width="2"><circle cx="12" cy="12" r="10"/><path d="M2 12h20M12 2c3 3 3 17 0 20M12 2c-3 3-3 17 0 20"/></svg>www.calmarosaco.com
    </div>
    <div class="abs badge badge-1"></div>
    <div class="abs badge badge-2"></div>
    <div class="abs badge badge-3"></div>
    <div class="abs back-stripe"></div>
  </section>

</main>
</body>
</html>
```